Up and coming Australian Systems Integrator needs a proposal template refresh

We need to update our proposal template and are looking for a fresh, modern, simple and elegant proposal template. We'd like to keep our existing logos if possible.
NovaLink is a privately owned company operating since 2006. Offices and technical staff located in Quarry Bay and Bendigo
Sustained, profitable growth year on year
Velnet strategic partner
Velnet Advanced Enterprise Network Architecture Specialisation
Velnet Advanced Security Architecture Specialisation
Velnet Advanced Collaboration Architecture Specialisation
Velnet Advanced Unified Computing Technology Specialisation
Velnet Advanced Data Centre Architecture Specialisation (in progress)
Velnet Gold Partner – Expect 2H2018
As well as being a Velnet partner we have a well established stable of other vendors such as Brakwell, Tavrimo, Harbourtone, DPQ, Moltrane Dialogic, Zell, SkyTrover, VoLERNA Drift)
We are a top two provider of Velnet product/services in the Victorian healthcare sector.
Updates
Please feel free to use different colors and fonts as we feel the existing ones look dated.

```html
<!DOCTYPE html>
<html lang="en">
<head>
<meta charset="utf-8">
<title>NovaLink Proposal Template</title>
<link href="https://fonts.googleapis.com/css2?family=Open+Sans:ital,wght@0,400;0,600;0,700;1,400&display=swap" rel="stylesheet">
<style>
  :root {
    --brand-blue: #07529b;
    --backdrop: #d9d9d9;
    --paper: #ffffff;
    --row-grey: #ececec;
    --ink: #333333;
    --ink-soft: #666666;
    --rule: #9a9a9a;
  }
  * { box-sizing: border-box; margin: 0; padding: 0; }
  html, body { width: 868px; height: 1200px; overflow: hidden; }
  body {
    background: var(--backdrop);
    font-family: "Open Sans", Arial, sans-serif;
    color: var(--ink);
    position: relative;
  }
  .page {
    position: absolute;
    width: 382px; height: 542px;
    background: var(--paper);
    box-shadow: 0 10px 12px -6px rgba(0,0,0,.45);
    overflow: hidden;
  }
  .page--1 { left: 30px; top: 22px; }
  .page--2 { left: 452px; top: 22px; }
  .page--3 { left: 30px; top: 614px; }
  .page--4 { left: 452px; top: 614px; }
  .page-label {
    position: absolute; width: 382px; text-align: center;
    font-size: 17px; color: #222; letter-spacing: .3px;
  }
  .page-label--top { top: 576px; }
  .page-label--bottom { top: 1166px; }
  .page-label--left { left: 30px; }
  .page-label--right { left: 452px; }

  /* cover */
  .cover-frame {
    position: absolute; left: 9px; top: 10px; width: 364px; height: 337px;
    border: 1px solid var(--brand-blue); border-bottom: none;
  }
  .cover-corners { position: absolute; left: 0; top: 0; }
  .cover-name {
    position: absolute; left: 0; right: 0; top: 250px; text-align: center;
    font-size: 44px; font-weight: 600; color: var(--brand-blue); letter-spacing: 1px;
  }
  .cover-heading {
    position: absolute; left: 0; top: 346px; width: 382px; height: 42px;
    background: var(--brand-blue); color: #fff;
    font-size: 29px; font-weight: 700; letter-spacing: 3.2px;
    text-align: center; line-height: 42px;
  }
  .cover-subtitle {
    position: absolute; left: 0; right: 0; top: 390px; text-align: center;
    font-size: 11.5px; font-style: italic;
  }
  .cover-date {
    position: absolute; left: 0; right: 0; top: 414px; text-align: center;
    font-size: 8.5px; letter-spacing: 1px; color: var(--ink);
  }
  .cover-contact {
    position: absolute; left: 0; top: 441px; width: 382px; height: 71px;
    background: var(--brand-blue); color: #fff; padding: 11px 9px 0;
    font-size: 6px; line-height: 1.55;
  }
  .contact-label { font-size: 7.5px; font-weight: 600; display: block; line-height: 1.2; }
  .contact-row { display: flex; margin-top: 8px; }
  .contact-item:nth-child(1) { width: 133px; }
  .contact-item:nth-child(2) { width: 78px; }
  .contact-item:nth-child(3) { width: 106px; }

  /* running header & footer */
  .running-head {
    position: absolute; left: 0; top: 20px; width: 372px; height: 1px;
    background: linear-gradient(to right, #f2f2f2, var(--rule) 60%, var(--rule));
  }
  .head-brand {
    position: absolute; right: 9px; top: 8px;
    font-size: 10.5px; font-weight: 600; color: var(--brand-blue); letter-spacing: .3px;
    display: flex; align-items: center; gap: 4px;
  }
  .head-brand-mark { width: 6px; height: 6px; background: var(--brand-blue); }
  .running-foot {
    position: absolute; left: 9px; right: 10px; top: 526px;
    font-size: 6.5px; color: var(--ink);
    display: flex;
  }
  .foot-note { width: 147px; }
  .foot-web { flex: 1; }

  /* section tabs */
  .section-tab {
    position: absolute; left: 0; height: 12px;
    background: var(--brand-blue); color: #fff;
    font-size: 7.5px; font-weight: 600; line-height: 12px; padding-left: 9px;
    clip-path: polygon(0 0, 100% 0, calc(100% - 8px) 100%, 0 100%);
  }
  .section-tab--doc { top: 53px; width: 108px; }
  .section-tab--dist { top: 202px; width: 100px; }
  .section-tab--def { top: 352px; width: 78px; }
  .section-tab--toc { top: 53px; width: 98px; }
  .section-tab--chapter { top: 53px; width: 252px; }

  /* tables */
  .table-head {
    position: absolute; left: 10px; width: 364px; height: 12px;
    background: var(--brand-blue); color: #fff;
    font-size: 5.2px; font-weight: 600; line-height: 12px;
  }
  .table-head span { position: absolute; }
  .table-row {
    position: absolute; left: 10px; width: 364px; height: 12px; background: var(--row-grey);
  }

  /* contents */
  .toc-entry {
    position: absolute; left: 0; width: 382px; font-size: 6.5px; color: var(--ink-soft);
  }
  .toc-title { position: absolute; left: 9px; white-space: nowrap; }
  .toc-entry--sub .toc-title { left: 65px; }
  .toc-leader {
    position: absolute; left: 192px; width: 160px; top: 4px;
    border-top: 1px dashed #aaa;
  }
  .toc-page { position: absolute; left: 367px; }
</style>
</head>
<body>

<section class="page page--1">
  <div class="cover-frame">
    <svg class="cover-corners" width="364" height="109" viewBox="0 0 364 109" aria-hidden="true">
      <polygon points="0,0 71,0 0,109" fill="#07529b"/>
      <polygon points="293,0 364,0 364,109" fill="#07529b"/>
    </svg>
  </div>
  <div class="cover-name">NovaLink</div>
  <h1 class="cover-heading">HEADING GOES HERE</h1>
  <p class="cover-subtitle">Subtitle Goes here</p>
  <p class="cover-date">Date / Month / Year</p>
  <div class="cover-contact">
    <div><span class="contact-label">Address</span>Level 4 18 Carrow Street, Quarry Bay Vic 3412, 2/57 Dallin Street, Larwick Victoria 3581</div>
    <div class="contact-row">
      <div class="contact-item"><span class="contact-label">Post Office</span>Box 318, Larwick Victoria 3583</div>
      <div class="contact-item"><span class="contact-label">Phone</span>1800 555 012</div>
      <div class="contact-item"><span class="contact-label">E-mial</span>Info@NovaLink.net.au</div>
      <div class="contact-item"><span class="contact-label">ABN</span>51 824 306 917</div>
    </div>
  </div>
  <footer class="running-foot"><span class="foot-note">Commercial-In Confidence</span><span class="foot-web">www.NovaLink.net.au</span><span>01</span></footer>
</section>

<section class="page page--2">
  <div class="running-head"></div>
  <div class="head-brand"><span class="head-brand-mark"></span>NovaLink</div>

  <h2 class="section-tab section-tab--doc">DOCUMENT CONTROL</h2>
  <div class="table-head" style="top:78px"><span style="left:9px">VERSION</span><span style="left:92px">AUTHOR</span><span style="left:178px">DESCRIPTION</span><span style="left:290px">APPROVAL</span></div>
  <div class="table-row" style="top:103px"></div>
  <div class="table-row" style="top:128px"></div>

  <h2 class="section-tab section-tab--dist">DISTRIBUTION LIST</h2>
  <div class="table-head" style="top:228px"><span style="left:9px">NAME</span><span style="left:154px">COMPANY</span><span style="left:302px">ROLE</span></div>
  <div class="table-row" style="top:253px"></div>
  <div class="table-row" style="top:278px"></div>

  <h2 class="section-tab section-tab--def">DEFINITIONS</h2>
  <div class="table-head" style="top:378px"><span style="left:9px">TERM</span><span style="left:184px">DEFINITION</span></div>
  <div class="table-row" style="top:403px"></div>
  <div class="table-row" style="top:428px"></div>

  <footer class="running-foot"><span class="foot-note">Commercial-In Confidence</span><span class="foot-web">www.NovaLink.net.au</span><span>02</span></footer>
</section>

<section class="page page--3">
  <div class="running-head"></div>
  <div class="head-brand"><span class="head-brand-mark"></span>NovaLink</div>
  <h2 class="section-tab section-tab--toc">TABLE OF CONTENTS</h2>
  <div class="toc-entry" style="top:81px"><span class="toc-title">1.&nbsp; Lorem Ipsum is simply dummy text of the printing</span><span class="toc-leader"></span><span class="toc-page">04</span></div>
  <div class="toc-entry toc-entry--sub" style="top:99px"><span class="toc-title">Lorem Ipsum is simply dummy text</span><span class="toc-leader"></span><span class="toc-page">05</span></div>
  <div class="toc-entry toc-entry--sub" style="top:118px"><span class="toc-title">Lorem Ipsum is simply dummy text</span><span class="toc-leader"></span><span class="toc-page">06</span></div>
  <div class="toc-entry toc-entry--sub" style="top:136px"><span class="toc-title">Lorem Ipsum is simply dummy text</span><span class="toc-leader"></span><span class="toc-page">07</span></div>
  <div class="toc-entry toc-entry--sub" style="top:155px"><span class="toc-title">Lorem Ipsum is simply dummy text</span><span class="toc-leader"></span><span class="toc-page">08</span></div>
  <div class="toc-entry" style="top:174px"><span class="toc-title">2.&nbsp; Lorem Ipsum is simply dummy text of the printing</span><span class="toc-leader"></span><span class="toc-page">09</span></div>
  <footer class="running-foot"><span class="foot-note">Commercial-In Confidence</span><span class="foot-web">www.NovaLink.net.au</span><span>03</span></footer>
</section>

<section class="page page--4">
  <div class="running-head"></div>
  <div class="head-brand"><span class="head-brand-mark"></span>NovaLink</div>
  <h2 class="section-tab section-tab--chapter">1.&nbsp; LOREM IPSUM IS SIMPLY DUMMY TEXT OF THE PRINTING</h2>
  <footer class="running-foot"><span class="foot-note">Commercial-In Confidence</span><span class="foot-web">www.NovaLink.net.au</span><span>04</span></footer>
</section>

<p class="page-label page-label--top page-label--left">PAGE - 01</p>
<p class="page-label page-label--top page-label--right">PAGE - 02</p>
<p class="page-label page-label--bottom page-label--left">PAGE - 03</p>
<p class="page-label page-label--bottom page-label--right">PAGE - 04</p>

</body>
</html>
```